Stationary design for boutique production house

We need a stationary design for our production house, 'Lorin Studios' based in Singapore. We produce microfilms as well as podcasts, talkshows and events. Our logo is a stylized icon of our director, who is also the executive producer and host of our programs, Lorin. Our main company colors are Red, Black and white. We would like a clean, minimalist design incorporating our existing company logo that conveys a sense of urbanism and elegance.

Logo and font files are attached. f

Target Market(s)

We focus on lifestyle media rather than entertainment.

Industry/Entity Type

Boutique

Font styles to use
Serif
Sans Serif

Colors
ec1f27
ffffff
000000

Requirements
Must have
• Our company logo and at least one of our company colors.
Nice to have
• Our address and contact information.
Should not have
• Changes made to the company logo (using only certain parts of it is fine though)

```html
<!DOCTYPE html>
<html lang="en">
<head>
<meta charset="utf-8">
<title>Lorin Studios — Stationery</title>
<link href="https://fonts.googleapis.com/css2?family=Bodoni+Moda:wght@500&family=Inter:wght@400;600&display=swap" rel="stylesheet">
<style>
  :root {
    --backdrop: #e8e8e8;
    --paper: #f5f5f5;
    --ink: #333333;
    --ink-soft: #555555;
    --charcoal: #3a3a3a;
    --red: #ec1f27;
    --white: #ffffff;
    --sans: "Inter", Arial, sans-serif;
    --serif: "Bodoni Moda", Georgia, serif;
  }
  * { box-sizing: border-box; margin: 0; padding: 0; }
  html, body { width: 1200px; height: 900px; overflow: hidden; }
  body { background: var(--backdrop); font-family: var(--sans); color: var(--ink); position: relative; }

  .sheet { position: absolute; background: var(--paper); box-shadow: 0 2px 6px rgba(0,0,0,.12); }

  .wordmark { font-family: var(--serif); font-weight: 500; color: var(--ink); text-transform: uppercase; letter-spacing: .04em; line-height: 1.05; display: flex; align-items: center; gap: 6px; }
  .wordmark .dot { width: 6px; height: 6px; border-radius: 50%; background: var(--red); flex: none; }

  .contact { font-size: 6px; line-height: 7.4px; color: var(--ink-soft); display: grid; grid-template-columns: 9px auto; }
  .contact .key { color: var(--red); }
  .contact .gap { height: 5px; grid-column: 1 / 3; }

  /* Letterhead */
  .letterhead { left: 252px; top: 112px; width: 331px; height: 469px; }
  .letterhead .wordmark { position: absolute; left: 24px; top: 60px; font-size: 10px; }
  .letterhead .contact { position: absolute; left: 219px; top: 25px; }
  .letter { position: absolute; left: 28px; top: 134px; width: 282px; font-size: 6.4px; line-height: 9.5px; color: var(--ink); }
  .letter p { margin-bottom: 9px; }
  .letter .topic { margin-bottom: 12px; }
  .letter .salutation, .letter .closing { font-weight: 600; }
  .signature { position: absolute; left: 28px; top: 378px; width: 96px; height: 28px; background: linear-gradient(90deg, #e4e7ec, #eef0f3); }
  .signatory { position: absolute; left: 28px; top: 412px; font-size: 6.4px; line-height: 7.5px; }
  .letterhead .site { position: absolute; right: 25px; top: 442px; font-size: 6px; color: var(--ink-soft); }

  /* Folder */
  .folder { left: 642px; top: 90px; width: 391px; height: 495px; }
  .folder .spine { position: absolute; top: 0; bottom: 0; width: 1px; background: #d4d4d4; }
  .folder .spine.a { left: 7px; } .folder .spine.b { left: 17px; }
  .folder .wordmark { position: absolute; left: 0; right: 0; top: 140px; justify-content: center; font-size: 20px; gap: 10px; }
  .folder .wordmark .dot { width: 12px; height: 12px; }
  .folder .site { position: absolute; left: 0; right: 0; top: 462px; text-align: center; font-size: 7px; color: var(--ink-soft); }

  /* Business cards */
  .card-front { left: 132px; top: 623px; width: 150px; height: 85px; }
  .card-front .wordmark { position: absolute; left: 70px; top: 34px; font-size: 8px; gap: 4px; }
  .card-front .wordmark .dot { width: 4px; height: 4px; }
  .card-front .site { position: absolute; right: -28px; top: 38px; transform: rotate(-90deg); font-size: 4px; color: var(--ink-soft); }

  .card-back { left: 132px; top: 733px; width: 150px; height: 84px; overflow: hidden; }
  .card-back .turned { position: absolute; left: 0; top: 84px; width: 84px; height: 150px; transform-origin: 0 0; transform: rotate(-90deg); padding: 8px 6px; }
  .card-back .person { font-size: 5.5px; font-weight: 600; line-height: 6px; }
  .card-back .role { font-size: 3.6px; color: var(--ink-soft); text-transform: uppercase; margin-bottom: 4px; }
  .card-back .contact { font-size: 3.6px; line-height: 4.4px; grid-template-columns: 5px auto; }
  .card-back .contact .gap { height: 2px; }
  .card-back .wordmark { position: absolute; left: 8px; bottom: 16px; font-size: 7px; gap: 4px; }
  .card-back .wordmark .dot { width: 4px; height: 4px; }

  /* Compliments slip */
  .slip { left: 321px; top: 636px; width: 371px; height: 177px; }
  .slip .wordmark { position: absolute; left: 17px; top: 40px; font-size: 13px; gap: 8px; }
  .slip .wordmark .dot { width: 8px; height: 8px; }
  .slip .contact { position: absolute; left: 8px; top: 133px; }

  /* Envelope */
  .envelope { left: 729px; top: 636px; width: 371px; height: 177px; }
  .envelope .flap { position: absolute; left: 0; top: 0; width: 100%; height: 62px; background: var(--charcoal); border-radius: 0 0 8px 8px; clip-path: polygon(0 0, 100% 0, 99% 100%, 1% 100%); display: flex; align-items: center; justify-content: center; }
  .envelope .flap .wordmark { color: var(--white); font-size: 10px; text-align: center; }
</style>
</head>
<body>

  <article class="sheet letterhead">
    <div class="wordmark">Lorin<br>Studios</div>
    <div class="contact">
      <span class="key">A</span><span>Postal Box 218</span>
      <span></span><span>Tiong Bahru 168730</span>
      <span></span><span>Unit 4 12 Seng Poh Rd</span>
      <span></span><span>Tiong Bahru 168730</span>
      <span class="gap"></span>
      <span class="key">M</span><span>6512 3048</span>
      <span class="key">E</span><span>ltay@lorin-studios.com</span>
    </div>
    <div class="letter">
      <p class="topic">Today's topic</p>
      <p class="salutation">Dear Mr. Hartono,</p>
      <p>Cras mattis consectetur purus sit amet fermentum. Etiam porta sem malesuada magna mollis euismod. Integer posuere erat a ante venenatis dapibus posuere velit aliquet. Cras justo odio, dapibus ac facilisis in, egestas eget quam. Aenean eu leo quam. Pellentesque ornare sem lacinia quam venenatis vestibulum.</p>
      <p>Donec id elit non mi porta gravida at eget metus. Fusce dapibus, tellus ac cursus commodo, tortor mauris condimentum nibh, ut fermentum massa justo sit amet risus. Cras justo odio, dapibus ac facilisis in, egestas eget quam. Cum sociis natoque penatibus et magnis dis parturient montes, nascetur ridiculus mus.</p>
      <p>Cum sociis natoque penatibus et magnis dis parturient montes, nascetur ridiculus mus. Curabitur blandit tempus porttitor. Aenean lacinia bibendum nulla sed consectetur. Lorem ipsum dolor sit amet, consectetur adipiscing elit.</p>
      <p>Cras justo odio, dapibus ac facilisis in, egestas eget quam. Morbi leo risus, porta ac consectetur ac, vestibulum at eros. Duis mollis, est non commodo luctus, nisi erat porttitor ligula, eget lacinia odio sem nec elit. Integer posuere erat a ante venenatis dapibus posuere velit aliquet. Vivamus sagittis lacus vel augue laoreet rutrum faucibus dolor auctor.</p>
      <p class="closing">Kind regards</p>
    </div>
    <div class="signature" role="img" aria-label="Handwritten signature of Lorin Tay"></div>
    <div class="signatory">Lorin Tay<br>Director</div>
    <div class="site">www.lorin-studios.com</div>
  </article>

  <article class="sheet folder">
    <span class="spine a"></span><span class="spine b"></span>
    <div class="wordmark"><span class="dot"></span>Lorin Studios</div>
    <div class="site">www.lorin-studios.com</div>
  </article>

  <article class="sheet card-front">
    <div class="wordmark"><span class="dot"></span>Lorin</div>
    <div class="site">www.lorin-studios.com</div>
  </article>

  <article class="sheet card-back">
    <div class="turned">
      <div class="person">Lorin Tay</div>
      <div class="role">Director</div>
      <div class="contact">
        <span class="key">A</span><span>Postal Box 218</span>
        <span></span><span>Tiong Bahru 168730</span>
        <span></span><span>Unit 4 12 Seng Poh Rd</span>
        <span class="gap"></span>
        <span class="key">M</span><span>6512 3048</span>
        <span class="key">E</span><span>ltay@lorin-studios.com</span>
      </div>
      <div class="wordmark"><span class="dot"></span>Lorin<br>Studios</div>
    </div>
  </article>

  <article class="sheet slip">
    <div class="wordmark"><span class="dot"></span>Lorin Studios</div>
    <div class="contact">
      <span class="key">A</span><span>Postal Box 218</span>
      <span></span><span>Tiong Bahru 168730</span>
      <span></span><span>Unit 4 12 Seng Poh Rd</span>
      <span></span><span>Tiong Bahru 168730</span>
    </div>
  </article>

  <article class="sheet envelope">
    <div class="flap"><div class="wordmark">Lorin<br>Studios</div></div>
  </article>

</body>
</html>
```